Social Media Graphics - ALL TEXT RK

We are looking for a series of social media graphics for Instagram (standard size 1:1 (1080x1080px) that are ALL TEXT. We want the following quotes below on each graphic; one quote per graphic. AND, In very small letters at the bottom of each graphic, add @RKMarlowLive

The look and feel of these graphics should be complimentary to the color palette attached below; but keep them simple. But the design is up to you; at the end of this document, I provided various samples of all text graphics that I like as examples.

Target Market(s)

women looking to lose weight

Industry/Entity Type

health and wellness

Colors
E54698
E96AAD
F1A4CE
F9D9EA
FCEFF6

Requirements
Must have
• the quotes in the document
Should not have
• no stock photography

```html
<!DOCTYPE html>
<html lang="en">
<head>
<meta charset="utf-8">
<title>Social Media Graphics – All Text Series</title>
<link rel="stylesheet" href="https://fonts.googleapis.com/css2?family=Libre+Baskerville:ital,wght@0,400;0,700;1,700&family=Cormorant+Garamond:wght@500&family=Great+Vibes&family=Staatliches&family=Comfortaa:wght@400&family=Yesteryear&family=Poppins:ital,wght@0,400;0,600;1,400;1,500&family=Lobster&family=Quicksand:wght@400;500&family=League+Gothic&family=Pathway+Gothic+One&display=swap">
<style>
  :root {
    --pink-500: #E54698;
    --pink-400: #E96AAD;
    --pink-300: #F1A4CE;
    --pink-200: #F9D9EA;
    --pink-100: #FCEFF6;
    --wine: #6e0b3a;
    --plum: #a3175e;
    --white: #ffffff;
    --line-light: rgba(255,255,255,0.45);
    --line-pink: #e8a2c6;
  }
  * { box-sizing: border-box; margin: 0; padding: 0; }
  html, body { width: 720px; height: 1200px; overflow: hidden; background: var(--white); }
  .sheet { position: relative; width: 720px; height: 1200px; }

  .post {
    position: absolute; width: 222px; height: 222px; overflow: hidden;
    color: var(--wine); text-align: center;
  }
  .col-a { left: 133px; } .col-b { left: 364px; }
  .row-1 { top: 27px; } .row-2 { top: 257px; } .row-3 { top: 488px; }
  .row-4 { top: 718px; } .row-5 { top: 949px; }

  .frame { position: absolute; inset: 8px; border: 1px solid var(--line-light); pointer-events: none; }
  .copy { position: absolute; left: 10px; right: 10px; }

  .handle {
    position: absolute; left: 55px; bottom: 4px; width: 112px; height: 17px;
    border-radius: 8px 8px 0 8px;
    font-family: "Pathway Gothic One", sans-serif; font-size: 12.5px; line-height: 17px;
    text-align: center; letter-spacing: 0.1px;
  }
  .handle--plum { background: var(--plum); color: var(--white); }
  .handle--white { background: var(--white); color: var(--plum); }

  /* 1 */
  .post--overnight { background: radial-gradient(circle at 10% 5%, #ec6aad 0%, var(--pink-500) 60%); }
  .post--overnight .lead { top: 22px; font-family: "Cormorant Garamond", serif; font-weight: 500; font-size: 20px; line-height: 22px; letter-spacing: 0.3px; }
  .post--overnight .yes { top: 84px; height: 44px; font-family: "Great Vibes", cursive; font-size: 33px; line-height: 40px; }
  .post--overnight .punch { top: 132px; font-family: "Libre Baskerville", serif; font-weight: 700; font-size: 17.5px; line-height: 22px; }

  /* 2 */
  .post--bloating { background: linear-gradient(200deg, #ffffff 0%, var(--pink-200) 30%, #ef8fc3 60%, var(--pink-500) 100%); }
  .post--bloating .frame { border-color: rgba(229,70,152,0.5); }
  .post--bloating .copy { font-family: "Staatliches", sans-serif; font-size: 22px; line-height: 21.5px; letter-spacing: 1px; }
  .post--bloating .q { top: 24px; }
  .post--bloating .a { top: 100px; }

  /* 3 */
  .post--supplement { background: linear-gradient(115deg, var(--pink-500) 55%, #ea5ea5 56%, var(--pink-500) 100%); }
  .post--supplement .bubble { position: absolute; left: 11px; top: 11px; width: 202px; height: 132px; border: 1px solid var(--line-light); border-radius: 24px 0 40px 0; }
  .post--supplement .lead { top: 24px; font-family: "Comfortaa", sans-serif; font-size: 17px; line-height: 22px; letter-spacing: 1.3px; }
  .post--supplement .how { top: 150px; font-family: "Yesteryear", cursive; font-size: 29px; line-height: 34px; }

  /* 4 */
  .post--flatten { background: radial-gradient(ellipse at 120% 55%, #f2b3d6 0%, var(--pink-400) 45%, #e65aa2 100%); }
  .post--flatten .bracket { position: absolute; left: 10px; top: 124px; width: 202px; height: 88px; border: 1px solid var(--line-light); border-top: none; border-radius: 0 0 0 30px; }
  .post--flatten .lead { top: 14px; font-family: "Poppins", sans-serif; font-style: italic; font-size: 19px; line-height: 21px; }
  .post--flatten .and { top: 100px; font-family: "Great Vibes", cursive; font-size: 46px; line-height: 40px; }
  .post--flatten .tail { top: 144px; font-family: "Poppins", sans-serif; font-style: italic; font-size: 19px; line-height: 21px; }

  /* 5 */
  .post--hormones { background: linear-gradient(160deg, #ec8ec2 0%, var(--pink-300) 35%, #f0a6cf 100%); }
  .post--hormones .copy { font-family: "Lobster", cursive; font-size: 23px; line-height: 23px; }
  .post--hormones .top { top: 12px; }
  .post--hormones .bottom { top: 112px; }
  .post--hormones .rule { position: absolute; left: 42px; right: 42px; top: 100px; height: 1px; background: var(--white); }
  .post--hormones .flourish { position: absolute; left: 84px; top: 95px; width: 54px; height: 10px; border-radius: 5px; background: var(--white); }

  /* 6 */
  .post--frustrated { background: linear-gradient(180deg, var(--pink-100) 0%, #f4b4d6 40%, #ea63a9 80%, var(--pink-500) 100%); }
  .post--frustrated .outline { position: absolute; left: 10px; top: 10px; width: 202px; height: 88px; border: 1px solid var(--white); border-right: none; border-bottom: none; border-radius: 14px 0 0 14px; }
  .post--frustrated .outline-b { position: absolute; left: 178px; top: 97px; width: 34px; height: 115px; border: 1px solid var(--white); border-left: none; border-radius: 0 14px 14px 0; }
  .post--frustrated .lead { top: 19px; font-family: "Quicksand", sans-serif; font-weight: 500; font-size: 18px; line-height: 19px; }
  .post--frustrated .body { top: 85px; font-family: "Quicksand", sans-serif; font-weight: 500; font-size: 21px; line-height: 21.5px; }

  /* 7 */
  .post--fault { background: var(--pink-500); }
  .post--fault .lead { left: 22px; right: auto; top: 30px; text-align: left; font-family: "Poppins", sans-serif; font-size: 18px; line-height: 19px; transform: rotate(-8deg); transform-origin: left top; }
  .post--fault .aside { left: 95px; right: auto; top: 84px; text-align: left; font-family: "Poppins", sans-serif; font-size: 18px; line-height: 18.5px; transform: rotate(-8deg); transform-origin: left top; }
  .post--fault .arrow { position: absolute; left: 55px; top: 90px; }

  /* 8 */
  .post--lied { background: var(--pink-200); }
  .post--lied .frame { inset: 10px; border-color: var(--pink-500); }
  .post--lied .copy { top: 24px; font-family: "Poppins", sans-serif; font-weight: 600; font-size: 21px; line-height: 21.5px; color: #4a0726; }
  .post--lied .quote { font-style: italic; font-weight: 400; color: var(--wine); display: block; margin: 2px 0; }

  /* 9 */
  .post--natural { background: var(--pink-100); }
  .post--natural .frame { border-color: var(--pink-200); }
  .post--natural .copy { font-family: "Libre Baskerville", serif; font-style: italic; font-weight: 700; color: var(--plum); }
  .post--natural .lead { top: 30px; font-size: 16.5px; line-height: 19.5px; letter-spacing: 0.4px; }
  .post--natural .cta { top: 142px; font-size: 21px; line-height: 20px; letter-spacing: 0.5px; }

  /* 10 */
  .post--glp { background: var(--pink-500); }
  .post--glp .copy { font-family: "League Gothic", sans-serif; font-size: 26px; line-height: 22px; }
  .post--glp .lead { left: 24px; top: 20px; text-align: left; }
  .post--glp .secret { top: 90px; font-family: "Yesteryear", cursive; font-size: 26px; line-height: 28px; color: var(--white); text-align: center; left: 30px; }
  .post--glp .tail { top: 122px; right: 28px; text-align: right; }
</style>
</head>
<body>
<main class="sheet">

  <section class="post post--overnight col-a row-1">
    <div class="frame"></div>
    <p class="copy lead">WAKE UP<br>TOMORROW WITH<br>A FLATTER BELLY-</p>
    <p class="copy yes">Yes,</p>
    <p class="copy punch">THIS OVERNIGHT<br>REMEDY WORKS<br>LIKE MAGIC!</p>
    <div class="handle handle--plum">@RKMarlowLive</div>
  </section>

  <section class="post post--bloating col-b row-1">
    <div class="frame"></div>
    <p class="copy q">STRUGGLING WITH<br>BLOATING AND<br>BELLY FAT?</p>
    <p class="copy a">TRY THIS NATURAL<br>SOLUTION TONIGHT,<br>AND WAKE UP<br>FEELING LIGHTER!</p>
    <div class="handle handle--white">@RKMarlowLive</div>
  </section>

  <section class="post post--supplement col-a row-2">
    <div class="bubble"></div>
    <p class="copy lead">One supplement,<br>one night;<br>your belly bloat<br>could be gone by<br>morning.</p>
    <p class="copy how">Here's how it works!</p>
    <div class="handle handle--white">@RKMarlowLive</div>
  </section>

  <section class="post post--flatten col-b row-2">
    <div class="bracket"></div>
    <p class="copy lead">Finally-a natural<br>solution that<br>flattens your<br>belly</p>
    <p class="copy and">And</p>
    <p class="copy tail">eases stomach<br>bloat</p>
    <div class="handle handle--plum">@RKMarlowLive</div>
  </section>

  <section class="post post--hormones col-a row-3">
    <p class="copy top">Sis, your<br>hormones are<br>out of whack</p>
    <div class="rule"></div>
    <div class="flourish" role="img" aria-label="Small decorative flourish dividing the two lines"></div>
    <p class="copy bottom">that's why the<br>weight won't<br>budge!</p>
    <div class="handle handle--plum">@RKMarlowLive</div>
  </section>

  <section class="post post--frustrated col-b row-3">
    <div class="outline"></div>
    <div class="outline-b"></div>
    <p class="copy lead">Frustrated with<br>belly fat that won't<br>budge?</p>
    <p class="copy body">I've got the<br>solution that<br>finally worked for<br>me-no crazy<br>diets required.</p>
    <div class="handle handle--plum">@RKMarlowLive</div>
  </section>

  <section class="post post--fault col-a row-4">
    <p class="copy lead">That stubborn belly<br>fat isn't your fault</p>
    <p class="copy aside">here's<br>what no<br>one tells<br>you.</p>
    <svg class="arrow" width="40" height="100" viewBox="0 0 40 100" aria-hidden="true">
      <path d="M32 2 C8 20 0 55 14 93" fill="none" stroke="var(--wine)" stroke-width="1.6" stroke-linecap="round"/>
      <path d="M6 84 L14 94 L19 82" fill="none" stroke="var(--wine)" stroke-width="1.6" stroke-linecap="round" stroke-linejoin="round"/>
    </svg>
    <div class="handle handle--white">@RKMarlowLive</div>
  </section>

  <section class="post post--lied col-b row-4">
    <div class="frame"></div>
    <p class="copy">You've been<br>lied to<span class="quote">'just eat less<br>and exercise<br>more'</span>doesn't work in<br>menopause</p>
    <div class="handle handle--plum">@RKMarlowLive</div>
  </section>

  <section class="post post--natural col-a row-5">
    <div class="frame"></div>
    <p class="copy lead">A natural way to<br>boost GLP-1 - no<br>injections, no side<br>effects, just real<br>results.</p>
    <p class="copy cta">HERE'S HOW<br>IT WORKS</p>
    <div class="handle handle--plum">@RKMarlowLive</div>
  </section>

  <section class="post post--glp col-b row-5">
    <div class="frame"></div>
    <p class="copy lead">GLP-1: THE MAGIC<br>BEHIND THE WEIGHT<br>LOSS DRUGS.</p>
    <p class="copy secret">But here's the secret</p>
    <p class="copy tail">YOU CAN BOOST IT<br>NATURALLY WITHOUT A<br>PRESCRIPTION!</p>
    <div class="handle handle--white">@RKMarlowLive</div>
  </section>

</main>
</body>
</html>
```